New company business cards with new company logo

We need a new business card designed as we have a new company logo and are going for a more 'flat design' look. Our company name is Veridanto and we are a global data focused Clinical Research Organisation. We'd ideally like one side with room for the individuals contact details, our full logo and our services - and one side which is quite plain, for example perhaps using the green triangular image attached with just the white 'V' in the center (also attached).

Industry/Entity Type

Business

Requirements
Must have
• Our main colour: #42b5a9
Please make text dark grey: #373737

```html
<!DOCTYPE html>
<html lang="en">
<head>
<meta charset="utf-8">
<title>Veridanto business cards</title>
<link rel="stylesheet" href="https://fonts.googleapis.com/css2?family=Open+Sans:wght@400;600&display=swap">
<style>
  :root {
    --teal: #42b5a9;
    --ink: #373737;
    --band: #3a3a3a;
    --paper: #ffffff;
    --table: #e3e4e4;
    --light: #f2f2f2;
  }
  * { margin: 0; padding: 0; box-sizing: border-box; }
  html, body { width: 1200px; height: 771px; overflow: hidden; }
  body {
    background: var(--table);
    font-family: "Open Sans", Arial, sans-serif;
    color: var(--ink);
    position: relative;
  }
  .card {
    position: absolute;
    top: 230px;
    width: 540px;
    height: 310px;
    background: var(--paper);
    box-shadow: 0 6px 18px rgba(0,0,0,.18);
    overflow: hidden;
  }
  .card--front { left: 40px; }
  .card--back { left: 620px; }

  /* Front: name block */
  .name-block {
    position: absolute;
    left: 0; right: 0; top: 58px;
    display: flex; flex-direction: column; align-items: center;
    text-align: center;
  }
  .name-block__dot {
    width: 72px; height: 72px; border-radius: 50%;
    background: var(--teal);
    margin-bottom: 22px;
  }
  .name-block__name {
    font-size: 54px; font-weight: 400; line-height: 1;
    letter-spacing: -.5px;
  }
  .name-block__line {
    font-size: 17px; letter-spacing: 1px; margin-top: 12px;
  }

  /* Back */
  .back-art { position: absolute; inset: 0; }
  .back-name {
    position: absolute; right: 30px; top: 26px;
    text-align: right;
  }
  .back-name__name {
    font-size: 38px; line-height: 1; letter-spacing: -.3px;
  }
  .back-name__line { font-size: 12.5px; letter-spacing: .8px; margin-top: 8px; }

  .contact {
    position: absolute; left: 22px; top: 128px;
    list-style: none;
    color: var(--light);
    font-size: 10.5px; line-height: 15px; letter-spacing: .6px;
  }
  .contact li { display: flex; align-items: flex-start; gap: 6px; }
  .contact svg { flex: none; margin-top: 2px; }
  .contact .indent { padding-left: 17px; }

  .person {
    position: absolute; right: 36px; bottom: 30px;
    text-align: right; color: var(--light);
    text-transform: uppercase;
  }
  .person__name { font-size: 13px; font-weight: 600; letter-spacing: 2.5px; }
  .person__role { font-size: 9.5px; letter-spacing: 3px; margin-top: 2px; }
</style>
</head>
<body>

<section class="card card--front" aria-label="Card front">
  <div class="name-block">
    <div class="name-block__dot"></div>
    <div class="name-block__name">Veridanto</div>
    <div class="name-block__line">Clinical Research Through Data</div>
  </div>
</section>

<section class="card card--back" aria-label="Card back">
  <svg class="back-art" viewBox="0 0 540 310" width="540" height="310" aria-hidden="true">
    <path d="M0 96 C150 110 300 160 540 262 L540 310 L0 310 Z" fill="var(--band)"/>
    <path d="M0 84 C170 96 320 150 470 222" fill="none" stroke="var(--teal)" stroke-width="7" stroke-linecap="round"/>
  </svg>

  <div class="back-name">
    <div class="back-name__name">Veridanto</div>
    <div class="back-name__line">Clinical Research Through Data</div>
  </div>

  <ul class="contact">
    <li>
      <svg width="11" height="11" viewBox="0 0 11 11"><circle cx="5.5" cy="5.5" r="5.5" fill="var(--light)"/><path d="M5.5 2.3a2 2 0 0 0-2 2c0 1.5 2 4 2 4s2-2.5 2-4a2 2 0 0 0-2-2z" fill="var(--band)"/></svg>
      <span>Unit 14, Harbor Court</span>
    </li>
    <li class="indent">Portvale 40218</li>
    <li>
      <svg width="11" height="11" viewBox="0 0 11 11"><circle cx="5.5" cy="5.5" r="5.5" fill="var(--light)"/><path d="M3.4 2.8l1.2-.3.6 1.5-.7.6c.3.8.9 1.4 1.7 1.7l.6-.7 1.5.6-.3 1.2C5.3 7.8 3.2 5.7 3.4 2.8z" fill="var(--band)"/></svg>
      <span>555-210-4471</span>
    </li>
    <li>
      <svg width="11" height="11" viewBox="0 0 11 11"><circle cx="5.5" cy="5.5" r="5.5" fill="var(--light)"/><rect x="3.6" y="2.3" width="3.8" height="6.4" rx=".7" fill="var(--band)"/></svg>
      <span>555-318-0926</span>
    </li>
    <li>
      <svg width="11" height="11" viewBox="0 0 11 11"><circle cx="5.5" cy="5.5" r="5.5" fill="var(--light)"/><path d="M3.4 2.8l1.2-.3.6 1.5-.7.6c.3.8.9 1.4 1.7 1.7l.6-.7 1.5.6-.3 1.2C5.3 7.8 3.2 5.7 3.4 2.8z" fill="var(--band)"/></svg>
      <span>555-642-7753</span>
    </li>
    <li>
      <svg width="11" height="11" viewBox="0 0 11 11"><circle cx="5.5" cy="5.5" r="5.5" fill="var(--light)"/><rect x="2.6" y="3.5" width="5.8" height="4" fill="var(--band)"/><path d="M2.6 3.5l2.9 2.2 2.9-2.2" fill="none" stroke="var(--light)" stroke-width=".6"/></svg>
      <span>mail@veridanto-cro.test</span>
    </li>
    <li>
      <svg width="11" height="11" viewBox="0 0 11 11"><circle cx="5.5" cy="5.5" r="5.5" fill="var(--light)"/><circle cx="5.5" cy="5.5" r="2.8" fill="none" stroke="var(--band)" stroke-width=".8"/><path d="M2.7 5.5h5.6M5.5 2.7v5.6" stroke="var(--band)" stroke-width=".6"/></svg>
      <span>www.veridanto-cro.test</span>
    </li>
  </ul>

  <div class="person">
    <div class="person__name">Marcus Hale</div>
    <div class="person__role">Owner / C.E.O</div>
  </div>
</section>

</body>
</html>
```